WordPress Classical Pianist Website, one pager with one one-pager as a subsite

Hi everyone,

I'm looking for a long-term freelance designer to refresh and modernize my existing WordPress website (www.velharo.com).
The new layout should be a clean one-page design with one one-pager subpage (CD's subpage).

From time to time, I also need help with smaller design projects such as concert flyers, CD covers (including booklets), and other promotional materials — that’s why I’m looking for a long-term collaboration.

The website is fully functional; I just need a fresh visual update that matches the style of my new CD and future materials.

Experience with WordPress is essential.
I'm looking for someone reliable, creative, and easy to communicate with — not a large agency.

Thanks a lot!
Tobias

Target Market(s)

Classical music audience, concert organizers (!), music students/music universities and piano music lovers worldwide.

Industry/Entity Type

Classical Music / Artist Portfolio

Coding

Coded - Design and coding required

Number of Pages Required

2 page

Other font styles liked:
• Ephesis Bold, Lexend Tera, Lexend Tera Medium, Adobe Fnt23

Requirements
Must have
• Clean and elegant one-page layout with 1–2 subpages (Bio, Concerts, Contact); high-quality visual design reflecting a professional concert pianist’s identity; visual harmony with my new CD “Sotto la Bruma” (colors, mood, tone); integration of photos, videos, CD covers, and short audio samples via a mini audio player; all existing content to be transferred from www.velharo.com ; bilingual structure (German/English); responsive design (desktop + mobile); built on WordPress
Nice to have
• Subtle animations or transitions between sections (smooth scrolling or fade-ins), elegant typography inspired by classical music aesthetics (fonts below), optional dark / light mode design, small music/video player or integrated streaming links (Tunevale, Cedar Sound, ClipHarbor)
Should not have
• Overloaded or cluttered layout, flashy or bright color schemes, stock photos unrelated to piano or classical music, heavy animations or slow loading times, generic, template-looking WordPress themes

```html
<!DOCTYPE html>
<html lang="de">
<head>
<meta charset="utf-8">
<title>Tobias Velharo – Konzertpianist</title>
<link rel="stylesheet" href="https://fonts.googleapis.com/css2?family=Bodoni+Moda:wght@400;500&family=Ephesis&family=Raleway:wght@400;700&display=swap">
<style>
  :root {
    --page: #f6efe9;
    --peach: #e9a375;
    --peach-deep: #d08552;
    --panel: #5b2d13;
    --ink: #120904;
    --white: #ffffff;
    --ghost: rgba(255, 225, 200, 0.30);
  }
  * { box-sizing: border-box; margin: 0; padding: 0; }
  html, body { width: 1200px; height: 805px; overflow: hidden; background: var(--page); }
  .site {
    position: absolute; left: 0; top: 65px;
    width: 1691px; height: 950px;
    transform: scale(0.70964); transform-origin: 0 0;
    overflow: hidden;
    font-family: "Raleway", sans-serif;
    background: linear-gradient(100deg, var(--peach-deep) 0%, var(--peach) 40%, #e7a070 75%, #e29a69 100%);
  }
  .backdrop-photo {
    position: absolute; left: 560px; top: 0; width: 1131px; height: 950px;
    background:
      radial-gradient(ellipse 380px 480px at 860px 330px, rgba(165, 95, 55, 0.30), transparent 70%),
      linear-gradient(180deg, rgba(190, 110, 65, 0.18), transparent 60%);
  }
  .hero-photo {
    position: absolute; left: 0; top: 0; width: 980px; height: 950px;
    background:
      radial-gradient(ellipse 230px 330px at 430px 620px, rgba(22, 14, 12, 0.88), rgba(22, 14, 12, 0.55) 60%, transparent 100%),
      radial-gradient(ellipse 560px 260px at 300px 900px, rgba(110, 30, 12, 0.90), transparent 80%),
      linear-gradient(135deg, rgba(130, 60, 28, 0.55) 0%, rgba(205, 130, 80, 0.25) 40%, transparent 70%),
      linear-gradient(90deg, rgba(150, 80, 45, 0.35) 0%, rgba(150, 80, 45, 0.15) 60%, transparent 100%);
  }
  .brand-mark {
    position: absolute; left: 45px; top: 30px;
    font-family: "Bodoni Moda", serif; font-size: 34px; line-height: 36px; color: var(--ink); letter-spacing: -0.5px;
  }
  .brand-mark span { display: block; }
  .brand-mark span + span { padding-left: 32px; }
  .languages { position: absolute; left: 1559px; top: 20px; display: flex; gap: 23px; }
  .languages svg { width: 33px; height: 20px; display: block; }
  .ghost-name {
    position: absolute; left: 1572px; top: 950px; width: 870px;
    transform: rotate(-90deg); transform-origin: 0 0;
    font-family: "Raleway", sans-serif; font-weight: 700; font-size: 112px; line-height: 120px;
    color: var(--ghost); white-space: nowrap; letter-spacing: -3px;
  }
  .title {
    position: absolute; left: 592px; top: 108px;
    font-family: "Bodoni Moda", serif; font-weight: 500; font-size: 145px; line-height: 128px;
    color: var(--ink); letter-spacing: -5px;
  }
  .title span { display: block; }
  .title span + span { padding-left: 200px; }
  .subtitle {
    position: absolute; left: 730px; top: 285px;
    font-family: "Ephesis", cursive; font-size: 165px; line-height: 1; color: var(--white);
  }
  .intro {
    position: absolute; left: 779px; top: 460px; width: 565px;
    font-size: 18px; line-height: 22px; color: var(--white);
  }
  .signature {
    position: absolute; left: 785px; top: 575px; width: 245px; height: 80px;
    background: rgba(255, 255, 255, 0.12);
    border-radius: 4px;
  }
  .release {
    position: absolute; left: 1050px; top: 585px; width: 641px; height: 238px;
    background: var(--panel);
  }
  .release-cover {
    position: absolute; left: 37px; top: 27px; width: 187px; height: 190px;
    background: linear-gradient(180deg, #d9c6a6 0%, #6b4d3a 45%, #111 100%);
  }
  .release-disc {
    position: absolute; left: 202px; top: 35px; width: 180px; height: 180px; border-radius: 50%;
    background: radial-gradient(circle, #b9b9b9 0 18px, #8d8d8d 19px 32px, transparent 33px), linear-gradient(180deg, #d8c5a4 0%, #5d4233 50%, #111 100%);
  }
  .release-title {
    position: absolute; left: 415px; top: 77px;
    font-weight: 700; font-size: 24px; line-height: 29px; color: var(--white); text-transform: uppercase;
  }
  .footer {
    position: absolute; left: 1005px; top: 905px;
    display: flex; align-items: center; gap: 28px;
    font-size: 15px; color: var(--ink);
  }
  .social { display: flex; gap: 16px; }
  .social span { display: flex; align-items: center; gap: 6px; font-size: 15px; }
  .social span::before { content: ""; width: 18px; height: 18px; border-radius: 50%; background: var(--ink); }
</style>
</head>
<body>
<main class="site">
  <div class="backdrop-photo" role="img" aria-label="Faded warm toned portrait of the pianist and piano interior in the background"></div>
  <div class="hero-photo" role="img" aria-label="Photograph of the pianist in a dark suit leaning on an open grand piano"></div>

  <div class="brand-mark"><span>TOBIAS</span><span>VELHARO</span></div>

  <nav class="languages" aria-label="Sprache">
    <svg viewBox="0 0 33 20" aria-label="Deutsch"><rect width="33" height="7" fill="#000"/><rect y="7" width="33" height="6" fill="#d00"/><rect y="13" width="33" height="7" fill="#fc0"/></svg>
    <svg viewBox="0 0 33 20" aria-label="English"><rect width="33" height="20" fill="#fff"/><g fill="#c22"><rect width="33" height="2"/><rect y="4" width="33" height="2"/><rect y="8" width="33" height="2"/><rect y="12" width="33" height="2"/><rect y="16" width="33" height="2"/></g><rect width="14" height="10" fill="#3c3b6e"/></svg>
  </nav>

  <div class="ghost-name">TOBIAS VELHARO</div>

  <h1 class="title"><span>TOBIAS</span><span>VELHARO</span></h1>
  <p class="subtitle">Konzertpianist</p>

  <p class="intro">Lorem ipsum dolor sit amet, consectetur adipiscing elit, sed do eiusmod tempor incididunt ut labore et dolore magna aliqua. Quis ipsum suspendisse ultrices gravida. Risus commodo viverra maecenas accumsan lacus vel facilisis.</p>
  <div class="signature" role="img" aria-label="Handwritten signature of the pianist"></div>

  <section class="release">
    <div class="release-cover" role="img" aria-label="CD cover of Sotto la Bruma with the pianist's portrait"></div>
    <div class="release-disc" role="img" aria-label="CD disc of Sotto la Bruma"></div>
    <h2 class="release-title">Lindqvist<br>Mazurkas<br>CD Release</h2>
  </section>

  <footer class="footer">
    <span>Tobias Velharo © All rights reserved</span>
    <span>Imprint | Privacy Policy</span>
    <div class="social"><span>Friendlane</span><span>Linkwork</span></div>
  </footer>
</main>
</body>
</html>
```